Quillfern Nightclub Flyer (Updated)

Flyer for facebook, square is fine, or rectangular. Here is the text:
QUILLFERN
Nightclub + Lounge
presents

SPLIT DECK WEDNESDAY
Nov 29 2018

CLUB FLOOR:
GORDY B2B RALPH
THEODORE BRUSKVIK

LOUNGE:
OTIS B2B HALF TIDE
COPPER FENWICK

Powered by HALVERN Acoustics
4716 Larchmere Avenue 21+ 9pm-2am
quillfernvenue-example.com for VIP booth inquiries

Target Market(s)

Nightclub

Industry/Entity Type

Night Club

Font styles to use
Sans Serif

Colors

Designer to choose colors to be used in the design.

Requirements
Must have
• All the text listed, and plz keep the theme of the attached files. We want to stay consistent with the Quillfern brand
Nice to have
• Try to stay with the theme from the attachments
Should not have
• Dont' stray to far from the general theme we have from the attachments

```html
<!DOCTYPE html>
<html lang="en">
<head>
<meta charset="utf-8">
<title>Quillfern Nightclub + Lounge — Split Deck Wednesday</title>
<link rel="stylesheet" href="https://fonts.googleapis.com/css2?family=Bodoni+Moda:wght@400;700&family=Montserrat:wght@300;400;600;700&display=swap">
<style>
  :root {
    --bg: #000000;
    --ink: #ffffff;
    --gold: #c9a063;
    --gold-light: #f4cf8a;
    --gold-dark: #9a7038;
    --band-text: #0c0a07;
  }
  * { margin: 0; padding: 0; box-sizing: border-box; }
  html, body { width: 1200px; height: 1200px; overflow: hidden; background: var(--bg); }
  .flyer {
    position: relative;
    width: 1200px;
    height: 1200px;
    background: var(--bg);
    font-family: "Montserrat", sans-serif;
    color: var(--ink);
    overflow: hidden;
  }
  .frame, .ornament { position: absolute; left: 0; top: 0; }
  .header { position: absolute; left: 0; right: 0; top: 112px; text-align: center; }
  .venue-name {
    font-family: "Bodoni Moda", serif;
    font-weight: 400;
    font-size: 104px;
    line-height: 1;
    letter-spacing: 2px;
    color: var(--ink);
  }
  .venue-sub {
    margin-top: 14px;
    font-weight: 400;
    font-size: 33px;
    letter-spacing: 5px;
    color: var(--ink);
  }
  .presents {
    margin-top: 30px;
    font-weight: 300;
    font-size: 28px;
    letter-spacing: 5px;
    color: var(--gold);
  }
  .event-band {
    position: absolute;
    left: 600px;
    top: 379px;
    transform: translateX(-50%);
    padding: 0 38px;
    height: 78px;
    display: flex;
    align-items: center;
    background: linear-gradient(90deg, var(--gold-dark) 0%, var(--gold-light) 50%, var(--gold-dark) 100%);
    color: var(--band-text);
    font-weight: 700;
    font-size: 50px;
    letter-spacing: 1px;
    white-space: nowrap;
  }
  .event-date {
    position: absolute;
    left: 0;
    right: 0;
    top: 474px;
    text-align: center;
    font-weight: 300;
    font-size: 26px;
    line-height: 34px;
    letter-spacing: 5px;
    color: var(--gold);
  }
  .room { position: absolute; left: 427px; width: 584px; }
  .room--club { top: 547px; }
  .room--lounge { top: 745px; }
  .room-label {
    display: inline-block;
    border: 1.5px solid var(--gold);
    padding: 6px 12px 4px;
    font-family: "Bodoni Moda", serif;
    font-weight: 700;
    font-size: 35px;
    line-height: 1.25;
    background: linear-gradient(90deg, var(--gold-light), var(--gold-dark));
    -webkit-background-clip: text;
    background-clip: text;
    color: transparent;
  }
  .room-rule { margin-top: 17px; height: 1.5px; background: var(--gold-dark); }
  .lineup { margin-top: 12px; padding-left: 8px; list-style: none; }
  .lineup li { font-size: 22px; line-height: 29px; letter-spacing: 0.5px; color: var(--ink); }
  .closing-rule { position: absolute; left: 427px; width: 584px; top: 943px; height: 1.5px; background: var(--gold-dark); }
  .vip {
    position: absolute; left: 744px; top: 963px; transform: translateX(-50%);
    text-align: center; white-space: nowrap;
    font-weight: 300; font-size: 28px; line-height: 37px; letter-spacing: 3px;
    color: var(--gold);
  }
  .details {
    position: absolute; left: 744px; top: 1054px; transform: translateX(-50%);
    text-align: center; white-space: nowrap;
    font-weight: 400; font-size: 25px; line-height: 34px; color: var(--ink);
  }
</style>
</head>
<body>
<main class="flyer">
  <svg class="ornament" width="1200" height="1200" viewBox="0 0 1200 1200" role="img" aria-label="Gold mandala ornament in the lower left corner">
    <defs>
      <radialGradient id="ornamentGlow" cx="60" cy="960" r="410" gradientUnits="userSpaceOnUse">
        <stop offset="0" stop-color="#d9b070" stop-opacity="0.85"/>
        <stop offset="0.7" stop-color="#a87a3e" stop-opacity="0.55"/>
        <stop offset="1" stop-color="#6e4f26" stop-opacity="0.35"/>
      </radialGradient>
      <clipPath id="innerArea"><path d="M94 54 H1106 V94 H1146 V1106 H1106 V1146 H94 V1106 H54 V94 H94 Z"/></clipPath>
    </defs>
    <circle cx="60" cy="960" r="410" fill="url(#ornamentGlow)" clip-path="url(#innerArea)"/>
  </svg>

  <svg class="frame" width="1200" height="1200" viewBox="0 0 1200 1200" aria-hidden="true">
    <g fill="none" stroke="#c9a063" stroke-width="3">
      <path d="M78 38 H1122 V78 H1162 V1122 H1122 V1162 H78 V1122 H38 V78 H78 Z"/>
      <path d="M94 54 H1106 V94 H1146 V1106 H1106 V1146 H94 V1106 H54 V94 H94 Z"/>
    </g>
  </svg>

  <header class="header">
    <h1 class="venue-name">QUILLFERN</h1>
    <p class="venue-sub">NIGHTCLUB + LOUNGE</p>
    <p class="presents">presents</p>
  </header>

  <div class="event-band">SPLIT DECK WEDNESDAY</div>
  <p class="event-date">NOV 29 2018</p>

  <section class="room room--club">
    <h2 class="room-label">CLUB FLOOR</h2>
    <div class="room-rule"></div>
    <ul class="lineup">
      <li>GORDY B2B RALPH</li>
      <li>THEODORE BRUSKVIK</li>
    </ul>
  </section>

  <section class="room room--lounge">
    <h2 class="room-label">LOUNGE</h2>
    <div class="room-rule"></div>
    <ul class="lineup">
      <li>OTIS B2B HALF TIDE</li>
      <li>COPPER FENWICK</li>
    </ul>
  </section>

  <div class="closing-rule"></div>

  <p class="vip">QUILLFERNVENUE-EXAMPLE.COM<br>FOR VIP BOOTH INQUIRIES</p>

  <p class="details">Powered by HALVERN Acoustics<br>4716 Larchmere Avenue 21+ 9pm-2am</p>
</main>
</body>
</html>
```